Non Profit Company Looking For New Website

The website for Corvale Paddock Rehoming Society should offer the viewer beautiful photos that inspire condifence and joy and tap into our love of horses.

We would like to see a website that displays trust, quality and confidence. Needs to be responsive and mobile friendly for all browsers and coded for both Android & IOS.

READ ATTACHED WEBSITE TEMPLATE FOR COMPLETE DETAILS ON WHAT WE ARE LOOKING FOR.

Looking for recommmendations if we should use WordPress/WooCommerce for site or Wordpress with Shopify Plug in or just Shopify.

Must be both desktop and mobile friendly with fast page load speed. Need the ability to edit ourselves.

Industry/Entity Type

Non Profit

Coding

Coded - Design and coding required

Number of Pages Required

5+ page

Requirements
Must have
• We would like to see a website that displays trust, quality and confidence. Needs to be responsive and mobile friendly for all browsers and coded for both Android & IOS.

Looking for recommendations if we should use WordPress/WooCommerce for site or Wordpress with Shopify Plug in or just Shopify.

Logo Colour:
Pantone 7621 C

READ TEMPLATE THAT IS ATTACHED
Nice to have
• Like look of this website as a sample:
https://www.quillmanegallop.com/

Another similar non profit organization
https://brindlefieldrest.com/

```html
<!DOCTYPE html>
<html lang="en">
<head>
<meta charset="utf-8">
<title>Corvale Paddock Rehoming Society</title>
<link rel="stylesheet" href="https://fonts.googleapis.com/css2?family=Playfair+Display:ital,wght@0,400;0,700;1,400&family=Montserrat:wght@400;500;600;700&display=swap">
<style>
:root{
  --red:#c41f2e;
  --red-dark:#a81826;
  --ink:#1d1d1d;
  --text:#444;
  --grey-bg:#efefef;
  --topbar:#f3f3f3;
  --white:#fff;
  --black:#0b0b0b;
  --serif:'Playfair Display', Georgia, serif;
  --sans:'Montserrat', Arial, sans-serif;
}
*{box-sizing:border-box;margin:0;padding:0}
html,body{width:1200px;height:4152px;overflow:hidden}
body{position:relative;background:var(--white);font-family:var(--sans);color:var(--text)}
h1,h2{font-weight:400}
.abs{position:absolute}

/* header */
.topbar{left:0;top:0;width:1200px;height:68px;background:var(--topbar)}
.social{display:flex;gap:18px;position:absolute}
.social span{width:22px;height:22px;border-radius:50%;background:var(--red);display:block}
.social-top{left:798px;top:23px}
.social-foot{left:856px;top:3944px}
.social-foot span{background:var(--white)}
.top-phone{left:942px;top:21px;font-size:15px;font-weight:500;color:#555;display:flex;align-items:center;gap:8px}
.navbar{left:0;top:68px;width:1200px;height:58px;background:var(--red)}
.nav{position:absolute;left:355px;top:0;display:flex;height:58px}
.nav a{color:var(--white);text-decoration:none;font-size:13.5px;font-weight:700;line-height:58px;margin-right:74px;position:relative}
.nav a.active:after{content:"";position:absolute;left:-8px;right:-8px;bottom:0;height:3px;background:var(--white)}
.logo-box{left:126px;top:0;width:172px;height:174px;background:var(--white);box-shadow:0 3px 8px rgba(0,0,0,.15);text-align:center;padding-top:18px;z-index:3}
.logo-box .wordmark{font-family:var(--serif);color:var(--red);font-size:21px;line-height:1.25;letter-spacing:1px}
.logo-box .mark{width:34px;height:34px;border-radius:50%;background:var(--red);margin:10px auto}

/* hero */
.hero{left:0;top:126px;width:1200px;height:700px;background:linear-gradient(100deg,#6e7a3a 0%,#8e8a46 30%,#b7823f 55%,#a85a24 70%,#d7a85a 100%)}
.hero-title{left:126px;top:318px;font-family:var(--serif);font-style:italic;color:var(--white);font-size:45px;line-height:48px}
.hero-wave{left:0;top:700px;width:1200px;height:140px}

/* intro */
.intro-title{left:0;top:880px;width:1200px;text-align:center;font-family:var(--serif);color:var(--red);font-size:45px;letter-spacing:1px}
.divider{left:435px;top:948px;width:330px;height:24px}
.intro-text{left:0;top:988px;width:1200px;text-align:center;font-size:21px;line-height:33px;color:#555}

/* aftercare */
.grey-wave{left:0;top:1060px;width:1200px;height:740px}
.circle-photo{left:129px;top:1244px;width:402px;height:402px;border-radius:50%;background:radial-gradient(circle at 40% 40%,#8fa85a,#4d6a2e 60%,#2d2f24)}
.ring{left:100px;top:1215px;width:460px;height:460px}
.about-title{left:617px;top:1262px;font-family:var(--serif);color:var(--ink);font-size:35px;line-height:33px}
.about-title b{font-weight:700}
.about-rule{left:617px;top:1343px;width:76px;height:4px;background:var(--red)}
.about-text{left:620px;top:1370px;width:455px;font-size:14.5px;line-height:24px;color:#444}
.about-text p{margin-bottom:31px}
.btn-outline{display:block;border:2px solid var(--red);color:var(--red);font-weight:700;text-align:center;text-decoration:none;border-radius:2px}
.learn-btn{left:622px;top:1592px;width:285px;height:57px;line-height:53px;font-size:17px}

/* adopt */
.adopt-photo{left:612px;top:1760px;width:588px;height:560px;background:linear-gradient(90deg,rgba(240,240,238,0) 0%,#4a3a2a 25%,#8a6a48 55%,#e3a65a 100%)}
.adopt-fade{left:0;top:1760px;width:1200px;height:560px}
.adopt-title{left:150px;top:1868px;font-family:var(--serif);font-size:41px;color:var(--ink)}
.adopt-title b{font-weight:700}
.adopt-bar{left:150px;top:1942px;width:3px;height:50px;background:var(--red)}
.adopt-text{left:169px;top:1937px;width:440px;font-size:18px;line-height:31px;color:#333}
.btn-solid{display:block;background:var(--red);color:var(--white);font-weight:700;text-align:center;text-decoration:none;border-radius:3px}
.adopt-btn{left:150px;top:2030px;width:202px;height:58px;line-height:58px;font-size:17px}

/* horses */
.horses-title{left:0;top:2350px;width:1200px;text-align:center;font-family:var(--serif);font-size:41px;color:var(--ink)}
.horses-title b{font-weight:700}
.horses-rule{left:555px;top:2413px;width:76px;height:4px;background:var(--red)}
.horse{width:343px;height:243px;position:absolute;overflow:hidden}
.h1{left:72px;top:2466px;background:linear-gradient(160deg,#c9b98a,#b3702e 50%,#6f8c3a)}
.h2{left:433px;top:2466px;background:linear-gradient(160deg,#2d2a27,#5a3a26 50%,#1f1c1a)}
.h3{left:793px;top:2466px;background:linear-gradient(180deg,#9fb4c4 0%,#5f6e5a 45%,#222 60%,#c43a24 85%)}
.h4{left:72px;top:2727px;background:linear-gradient(160deg,#b35a2a,#4a2a1a 55%,#c07848)}
.h5{left:433px;top:2727px;background:linear-gradient(160deg,#d8dcc0,#a35a24 50%,#6a8a3a)}
.h6{left:793px;top:2727px;background:linear-gradient(160deg,#9a7a3a,#5a3a22 55%,#2f2a20)}
.horse-info{position:absolute;left:0;right:0;bottom:0;height:120px;padding:0 18px;background:linear-gradient(0deg,rgba(0,0,0,.65),rgba(0,0,0,0));color:var(--white)}
.horse-name{font-family:var(--serif);font-style:italic;font-size:25px;margin-top:12px;padding-bottom:9px;border-bottom:1px solid rgba(255,255,255,.6)}
.horse-meta{display:grid;grid-template-columns:1fr 1fr;font-size:11.5px;line-height:22px;margin-top:9px}
.horse-meta b{font-weight:700}
.give-btn{left:437px;top:3025px;width:335px;height:67px;line-height:63px;font-size:21px}

/* contact */
.contact-band{left:0;top:3141px;width:1200px;height:600px;background:linear-gradient(180deg,#c41f2e,#d22a35 60%,#c41f2e)}
.contact-title{left:0;top:3196px;width:1200px;text-align:center;font-family:var(--serif);color:var(--white);font-size:36px}
.contact-title b{font-weight:700}
.contact-rule{left:560px;top:3250px;width:74px;height:3px;background:var(--white)}
.contact-sub{left:0;top:3265px;width:1200px;text-align:center;color:var(--white);font-size:15px;font-weight:500}
.info-icon{width:64px;height:64px;border:2px solid var(--white);border-radius:50%;display:flex;align-items:center;justify-content:center}
.info{color:var(--white);font-size:13.5px;line-height:26px}
.info b{font-weight:700;display:block}
.field{border:1.5px solid var(--white);color:var(--white);font-size:12px;font-weight:500;padding:0 17px;display:flex;align-items:center;gap:8px}
.captcha{left:528px;top:3544px;width:200px;height:47px;background:#f9f9f9;border:1px solid #d5d5d5;border-radius:2px;font-size:9px;color:#333;display:flex;align-items:center;padding-left:10px;gap:8px}
.captcha i{width:17px;height:17px;border:2px solid #c1c1c1;background:#fff;border-radius:2px;display:block}
.captcha em{position:absolute;right:8px;top:8px;width:22px;height:22px;border-radius:50%;background:#4a90e2;display:block}
.submit{left:859px;top:3543px;width:170px;height:50px;background:#2e2e2e;color:var(--white);font-weight:700;font-size:16px;text-align:center;line-height:50px;border-radius:3px}
.contact-wave{left:0;top:3630px;width:1200px;height:120px}

/* footer */
.footer{left:0;top:3730px;width:1200px;height:346px;background:var(--black)}
.foot-logo{left:112px;top:3800px;width:180px;text-align:center;font-family:var(--serif);color:var(--white);font-size:24px;line-height:30px}
.foot-logo .mark{width:40px;height:40px;border-radius:50%;background:var(--white);margin:10px auto}
.foot-head{font-family:var(--serif);color:var(--white);font-size:16px;font-weight:700;letter-spacing:.5px;position:absolute}
.foot-head:after{content:"";display:block;width:56px;height:1px;background:#aaa;margin-top:7px}
.foot-links{left:356px;top:3840px;color:#ccc;font-size:12.5px;line-height:30px;list-style:none}
.foot-contact{left:550px;top:3842px;color:#ccc;font-size:12.5px;line-height:20px}
.foot-contact div{display:flex;gap:12px;margin-bottom:14px}
.foot-contact svg{flex:none}
.sub-input{left:857px;top:3842px;width:217px;height:36px;background:var(--white);font-size:11px;color:#888;padding-left:15px;line-height:36px;border-radius:2px}
.sub-btn{left:857px;top:3886px;width:217px;height:36px;background:var(--red);color:var(--white);font-family:var(--serif);font-weight:700;font-size:12px;text-align:center;line-height:36px;border-radius:2px}
.copy{left:0;top:4076px;width:1200px;height:76px;background:var(--black);border-top:1px solid #333;color:#bbb;font-size:12px;text-align:center;line-height:76px}
</style>
</head>
<body>

<header>
  <div class="abs topbar">
    <div class="social social-top" aria-label="Social links"><span aria-label="Social profile one"></span><span aria-label="Social profile two"></span><span aria-label="Social profile three"></span></div>
    <div class="abs top-phone">
      <svg width="22" height="22" viewBox="0 0 24 24"><path d="M6.6 10.8a15.1 15.1 0 0 0 6.6 6.6l2.2-2.2a1 1 0 0 1 1-.25 11.4 11.4 0 0 0 3.6.57 1 1 0 0 1 1 1V20a1 1 0 0 1-1 1A17 17 0 0 1 3 4a1 1 0 0 1 1-1h3.5a1 1 0 0 1 1 1c0 1.25.2 2.45.57 3.6a1 1 0 0 1-.25 1z" fill="var(--red)"/></svg>
      (780) 555-0142
    </div>
  </div>
  <nav class="abs navbar">
    <div class="nav">
      <a class="active" href="#">HOME</a><a href="#">ABOUT</a><a href="#">ADOPT</a><a href="#">HORSES</a><a href="#">DONATE</a><a href="#">CONTACT</a>
    </div>
  </nav>
  <div class="abs logo-box">
    <div class="wordmark">CORVALE</div>
    <div class="mark"></div>
    <div class="wordmark" style="font-size:14px;line-height:17px">PADDOCK<br>REHOMING</div>
  </div>
</header>

<section>
  <div class="abs hero" role="img" aria-label="Chestnut horse standing in a sunlit meadow"></div>
  <h1 class="abs hero-title">We support and develop retired<br>thoroughbred racehorses<br>for their next chapter in life</h1>
  <svg class="abs hero-wave" viewBox="0 0 1200 140" preserveAspectRatio="none">
    <path d="M0 140 L0 90 C250 20 500 60 720 80 C900 96 1060 80 1200 40 L1200 140 Z" fill="var(--red)"/>
    <path d="M0 140 L0 125 C250 45 500 80 720 95 C900 106 1060 92 1200 55 L1200 140 Z" fill="var(--white)"/>
  </svg>
</section>

<section>
  <h2 class="abs intro-title">RETIRE. RETRAIN.REHOME.</h2>
  <svg class="abs divider" viewBox="0 0 330 24"><line x1="0" y1="12" x2="150" y2="12" stroke="#ccc"/><line x1="180" y1="12" x2="330" y2="12" stroke="#ccc"/><circle cx="165" cy="12" r="5" fill="none" stroke="#bbb"/></svg>
  <p class="abs intro-text">Corvale Paddock Rehoming Society (CPRS) is a registered<br>not-for-profit organization in Alberta.</p>
</section>

<section>
  <svg class="abs grey-wave" viewBox="0 0 1200 740" preserveAspectRatio="none">
    <path d="M0 130 C300 50 600 150 900 140 C1050 135 1150 110 1200 90 L1200 620 C1000 690 800 700 600 690 C400 680 200 640 100 660 L0 680 Z" fill="var(--grey-bg)"/>
    <path d="M100 660 C300 600 500 650 700 680 C900 710 1080 680 1200 630 L1200 660 C1080 720 900 740 700 715 C500 690 300 650 100 665 Z" fill="var(--red)"/>
    <path d="M0 680 L100 665 C300 650 500 690 700 715 C900 740 1080 720 1200 660 L1200 740 L0 740 Z" fill="#f4f4f2"/>
  </svg>
  <svg class="abs ring" viewBox="0 0 460 460"><circle cx="230" cy="230" r="227" fill="none" stroke="#d98a92" stroke-width="1.5"/><circle cx="230" cy="230" r="218" fill="none" stroke="#d98a92" stroke-width="1.5"/></svg>
  <div class="abs circle-photo" role="img" aria-label="Rider in a helmet standing beside a dark bay horse"></div>
  <h2 class="abs about-title">WHAT IS THOROUGHBRED<br><b>AFTERCARE?</b></h2>
  <div class="abs about-rule"></div>
  <div class="abs about-text">
    <p>The health, safety and welfare of our equine athletes does not end at the finish line, and retirement and aftercare are critical to the success of the racing industry.</p>
    <p>Aftercare is the safe placement of racehorses after their careers as racehorse are completed. Some horses might retire to the breeding shed or broodmare bands, while others are retrained for second careers.</p>
  </div>
  <a class="abs btn-outline learn-btn" href="#">LEARN MORE ABOUT US</a>
</section>

<section>
  <div class="abs adopt-photo" role="img" aria-label="Young woman resting her head against a saddled dark horse at sunset"></div>
  <svg class="abs adopt-fade" viewBox="0 0 1200 560" preserveAspectRatio="none">
    <path d="M0 520 C300 560 600 540 800 520 C950 505 1100 480 1200 440 L1200 560 L0 560 Z" fill="var(--white)"/>
  </svg>
  <h2 class="abs adopt-title"><b>ADOPT</b> A HORSE</h2>
  <div class="abs adopt-bar"></div>
  <p class="abs adopt-text">Corvale Paddock Rehoming is committed to helping match you with the perfect horse.</p>
  <a class="abs btn-solid adopt-btn" href="#">ADOPT NOW</a>
</section>

<section>
  <h2 class="abs horses-title">OUR <b>HORSES</b></h2>
  <div class="abs horses-rule"></div>
  <div class="horse h1" role="img" aria-label="Chestnut horse with flowing mane in a green field"></div>
  <div class="horse h2" role="img" aria-label="Bay gelding in a bridle against a dark background">
    <div class="horse-info">
      <div class="horse-name">Copper Lane</div>
      <div class="horse-meta">
        <span><b>Birth Year</b>: 2018</span><span><b>Color:</b> Bay</span>
        <span><b>Gender:</b> Gelding</span><span><b>Location:</b> Halden, ON</span>
      </div>
    </div>
  </div>
  <div class="horse h3" role="img" aria-label="Black horse in a field of red poppies below hills"></div>
  <div class="horse h4" role="img" aria-label="Bay horse in a halter among autumn trees"></div>
  <div class="horse h5" role="img" aria-label="Bay horse trotting across a sunny paddock"></div>
  <div class="horse h6" role="img" aria-label="Horse grazing at dusk in golden light"></div>
  <a class="abs btn-outline give-btn" href="#">MORE WAYS TO GIVE</a>
</section>

<section>
  <div class="abs contact-band"></div>
  <h2 class="abs contact-title">DO YOU HAVE <b>ANY QUESTION</b></h2>
  <div class="abs contact-rule"></div>
  <p class="abs contact-sub">Give us a Call or use the contact form below</p>

  <div class="abs info-icon" style="left:155px;top:3338px"><svg width="28" height="28" viewBox="0 0 24 24"><path d="M12 2a7 7 0 0 0-7 7c0 5 7 13 7 13s7-8 7-13a7 7 0 0 0-7-7z" fill="none" stroke="#fff" stroke-width="1.5"/><circle cx="12" cy="9" r="2.5" fill="none" stroke="#fff" stroke-width="1.5"/></svg></div>
  <div class="abs info" style="left:238px;top:3339px"><b>ADDRESS</b>Brindle Creek, Alberta Canada<br>4120 RR 88, PO Box 2207</div>
  <div class="abs info-icon" style="left:155px;top:3443px"><svg width="28" height="28" viewBox="0 0 24 24"><path d="M6.6 10.8a15.1 15.1 0 0 0 6.6 6.6l2.2-2.2a1 1 0 0 1 1-.25 11.4 11.4 0 0 0 3.6.57 1 1 0 0 1 1 1V20a1 1 0 0 1-1 1A17 17 0 0 1 3 4a1 1 0 0 1 1-1h3.5a1 1 0 0 1 1 1c0 1.25.2 2.45.57 3.6a1 1 0 0 1-.25 1z" fill="none" stroke="#fff" stroke-width="1.5"/></svg></div>
  <div class="abs info" style="left:238px;top:3449px"><b>CALL US</b>(780) 555-0142</div>
  <div class="abs info-icon" style="left:155px;top:3530px"><svg width="30" height="24" viewBox="0 0 30 24"><rect x="2" y="3" width="26" height="18" fill="none" stroke="#fff" stroke-width="1.5"/><path d="M2 3l13 10 13-10" fill="none" stroke="#fff" stroke-width="1.5"/></svg></div>
  <div class="abs info" style="left:238px;top:3540px"><b>EMAIL US</b>info@corvalepaddock.org</div>

  <div class="abs field" style="left:522px;top:3340px;width:248px;height:42px">&#9679; First Name</div>
  <div class="abs field" style="left:780px;top:3340px;width:248px;height:42px">&#9679; Last Name</div>
  <div class="abs field" style="left:522px;top:3394px;width:248px;height:42px">&#9993; Email address</div>
  <div class="abs field" style="left:780px;top:3394px;width:248px;height:42px">&#9742; Phone</div>
  <div class="abs field" style="left:524px;top:3452px;width:504px;height:76px;align-items:flex-start;padding-top:14px">&#9679; How can we help you?</div>
  <div class="abs captcha"><i></i>I'm not a robot<em></em></div>
  <div class="abs submit">SUBMIT</div>

  <svg class="abs contact-wave" viewBox="0 0 1200 120" preserveAspectRatio="none">
    <path d="M0 30 C200 80 500 110 800 100 C950 95 1100 70 1200 40 L1200 120 L0 120 Z" fill="#8a8a8a"/>
    <path d="M0 55 C200 95 500 120 800 112 C950 108 1100 85 1200 55 L1200 120 L0 120 Z" fill="var(--black)"/>
  </svg>
</section>

<footer>
  <div class="abs footer"></div>
  <div class="abs foot-logo">CORVALE<div class="mark"></div><span style="font-size:16px;line-height:20px">PADDOCK<br>REHOMING</span></div>
  <div class="foot-head" style="left:356px;top:3796px">NAVIGATION</div>
  <ul class="abs foot-links"><li>About Us</li><li>Adopt</li><li>Horses</li><li>Donate</li><li>Contact Us</li></ul>
  <div class="foot-head" style="left:550px;top:3798px">CONTACT US</div>
  <div class="abs foot-contact">
    <div><svg width="16" height="20" viewBox="0 0 24 24"><path d="M12 2a7 7 0 0 0-7 7c0 5 7 13 7 13s7-8 7-13a7 7 0 0 0-7-7z" fill="#fff"/><circle cx="12" cy="9" r="2.5" fill="#000"/></svg><span>218 Marlow Avenue P.O. Box 47<br>Halden, Ontario &nbsp;K2P 4T1</span></div>
    <div><svg width="18" height="18" viewBox="0 0 24 24"><path d="M6.6 10.8a15.1 15.1 0 0 0 6.6 6.6l2.2-2.2a1 1 0 0 1 1-.25 11.4 11.4 0 0 0 3.6.57 1 1 0 0 1 1 1V20a1 1 0 0 1-1 1A17 17 0 0 1 3 4a1 1 0 0 1 1-1h3.5a1 1 0 0 1 1 1c0 1.25.2 2.45.57 3.6a1 1 0 0 1-.25 1z" fill="#fff"/></svg><span>Tel: (780) 555-0148</span></div>
    <div><svg width="20" height="16" viewBox="0 0 30 24"><rect x="2" y="3" width="26" height="18" fill="none" stroke="#fff" stroke-width="2"/><path d="M2 3l13 10 13-10" fill="none" stroke="#fff" stroke-width="2"/></svg><span>Email: info@corvalepaddock.org</span></div>
  </div>
  <div class="foot-head" style="left:857px;top:3798px">FOLLOW US</div>
  <div class="abs sub-input">Your Email address</div>
  <div class="abs sub-btn">SUBSCRIBE</div>
  <div class="social social-foot" aria-label="Social links"><span aria-label="Social profile one"></span><span aria-label="Social profile two"></span><span aria-label="Social profile three"></span></div>
  <div class="abs copy">©2021 Copyright Corvale. All Right Reserved</div>
</footer>

</body>
</html>
```